Dog breeder design card

A card for our dog showing/breeding and companion puppy buyers.
Updates

Reason: The photo's I provided were not seen by designers because of a glitch or error, so I will need to start them over again in the designs submitted to me. I uploaded and emailed the photo's last night.

Thank you all so much for your lovely designs, I like wquite a few of them. I provided images in my original brief, but these apparently did not become available for you to see. I have emailed my images now, so hopefully you may be able to incorporate them into your designs.

Thank you so much for your time,
kind regards,
Beatrice

I have attached the photo’s that can hopefully be incorporated onto my business card. I don’t mind if the whole images aren’t used, but maybe a soft focus look around the adult dog and in a corner of the card maybe....if that’s possible.

Contact Information for Business Card

Corvanel Bullmastiffs, adored by Gerald and Beatrice Lindqvist.
Tallowmere KVR
0478 552961

Requirements
Nice to have
• Soft focus look to the outline of adult dogs head incorporated into perhaps a corner of the card. Soft focus outline around pups perhaps.
I do really love hot pink and/or purple text if possible.
"Corvanel Bullmastiffs" to be incorporated on the front of card, our details on reverse.
Would prefer a glossy finish rather than matt.

```html
<!DOCTYPE html>
<html lang="en">
<head>
<meta charset="utf-8">
<title>Corvanel Bullmastiffs – Business Card</title>
<link rel="stylesheet" href="https://fonts.googleapis.com/css2?family=Exo+2:wght@300;400;800&display=swap">
<style>
  :root {
    --page: #ffffff;
    --card: #ffffff;
    --ink-grey: #6d6e71;
    --ink-magenta: #a3218e;
    --art-light: #f3f3f4;
    --art-mid: #d9dadb;
    --card-shadow: rgba(0, 0, 0, 0.22);
  }
  * { box-sizing: border-box; margin: 0; padding: 0; }
  html, body {
    width: 1200px;
    height: 894px;
    overflow: hidden;
    background: var(--page);
  }
  .canvas {
    position: relative;
    width: 1200px;
    height: 894px;
    font-family: "Exo 2", sans-serif;
  }
  .card {
    position: absolute;
    width: 658px;
    height: 385px;
    background: var(--card);
    box-shadow: 0 10px 22px var(--card-shadow);
    overflow: hidden;
  }
  .card--front { left: 40px; top: 37px; }
  .card--back  { left: 511px; top: 476px; }

  .portrait {
    position: absolute;
    left: 363px;
    top: 17px;
    width: 295px;
    height: 368px;
    background: radial-gradient(ellipse at 45% 40%, var(--art-light) 0%, var(--art-mid) 100%);
    border-radius: 46% 42% 0 0 / 30% 30% 0 0;
  }

  .brand {
    position: absolute;
    left: 34px;
    top: 270px;
    color: var(--ink-grey);
  }
  .brand__name {
    display: block;
    font-weight: 800;
    font-size: 41px;
    line-height: 1;
    letter-spacing: 0.25em;
    color: var(--ink-magenta);
  }
  .brand__breed {
    display: block;
    font-weight: 300;
    font-size: 43px;
    line-height: 1;
    letter-spacing: 0.105em;
    margin-top: 2px;
  }

  .contact {
    position: absolute;
    right: 34px;
    bottom: 30px;
    text-align: right;
    font-weight: 400;
    font-size: 23.5px;
    line-height: 29px;
    color: var(--ink-grey);
  }
  .contact__name { color: var(--ink-magenta); }
</style>
</head>
<body>
<main class="canvas">
  <section class="card card--front" aria-label="Card front">
    <div class="portrait" role="img" aria-label="Line illustration of a bullmastiff's head and chest in grey outline"></div>
    <h1 class="brand">
      <span class="brand__name">CORVANEL</span>
      <span class="brand__breed">bullmastiffs</span>
    </h1>
  </section>

  <section class="card card--back" aria-label="Card back">
    <p class="contact">
      Adored by <span class="contact__name">Gerald</span> and <span class="contact__name">Beatrice Lindqvist</span><br>
      Tallowmere KVR 0478 552961
    </p>
  </section>
</main>
</body>
</html>
```